PowerPoint Design

We require a sample PowerPoint design so we can pitch PPT design services to a client.

The designs do NOT need to be done in PowerPoint, but should reflect designs that *could* be created in PPT format.

We require 3 slides as part of this project:

1. A slide containing the statistical chart based on data in Figure 3.3 at http://www7.dovrimark.org/survey-releves/2006/tb-qr/ab-cd/index.cfm?LANG=ENG&VIEW=C&format=flash&PRCODE=01&TOPIC_ID=2
-> note, don't just copy and paste the existing graph - come up with something innovative and eye catching

2. Inspirational slide to motivate employees. Zorvex "inspirational quote" and select a quote you think is appropriate. Imagery should generate enthusiasm/optimism.

3. A slide of your own choosing.
Updates

Project Deadline Extended
Reason: One of the team reviewing the designs is away from office. We've decided to give other designers a chance to submit ideas. Final decision will be made on December 5th, 2011.

Target Market(s)

Business professionals

Industry/Entity Type

Zorvex

Requirements
Must have
• Must have 3 slides.

```html
<!DOCTYPE html>
<html lang="en">
<head>
<meta charset="utf-8">
<title>Slide title</title>
<link rel="stylesheet" href="https://fonts.googleapis.com/css2?family=Carlito:wght@400;700&display=swap">
<style>
  :root {
    --band-teal: #1b8db4;
    --band-teal-dark: #137aa0;
    --band-red: #c8300c;
    --band-red-dark: #a82608;
    --text-grey: #6a6a6a;
    --bullet-red: #c8300c;
    --chart-title: #1a9ad6;
    --frame-blue: #2aa6d8;
    --q1: #0e6a8c;
    --q2: #14aadb;
    --q3: #80d8f3;
    --q4: #d2300e;
    --bg-top: #ffffff;
    --bg-bottom: #d6d6d6;
    --below-footer: #dcdcdc;
  }
  * { box-sizing: border-box; margin: 0; padding: 0; }
  html, body { width: 1200px; height: 900px; overflow: hidden; }
  body {
    font-family: "Carlito", "Calibri", sans-serif;
    background: linear-gradient(to bottom, var(--bg-top) 0%, var(--bg-top) 32%, var(--bg-bottom) 100%);
    position: relative;
  }
  .title-band {
    position: absolute; left: 0; top: 25px; width: 1200px; height: 104px;
    background: linear-gradient(to bottom, var(--band-teal), var(--band-teal-dark));
  }
  .slide-title {
    position: absolute; left: 72px; top: 22px;
    font-size: 52px; font-weight: 400; color: #fff; line-height: 1.2;
  }
  .body-text {
    position: absolute; left: 78px; top: 160px; width: 580px;
    list-style: none; color: var(--text-grey);
  }
  .body-text > li {
    position: relative; padding-left: 41px;
    font-size: 28px; line-height: 35px; margin-bottom: 7px;
  }
  .body-text li::before {
    content: ""; position: absolute; left: 0; top: 12px;
    width: 10px; height: 10px; background: var(--bullet-red);
  }
  .sub-list { list-style: none; margin-top: 6px; }
  .sub-list li {
    position: relative; padding-left: 36px;
    font-size: 23px; line-height: 30px; margin-bottom: 6px;
  }
  .sub-list li::before { top: 10px; width: 8px; height: 8px; left: 12px; }
  .chart-frame {
    position: absolute; left: 685px; top: 224px; width: 466px; height: 528px;
    border: 2px dashed var(--frame-blue);
  }
  .chart-frame svg { position: absolute; left: -2px; top: -2px; }
  .footer-band {
    position: absolute; left: 0; top: 838px; width: 1200px; height: 37px;
    background: linear-gradient(to bottom, var(--band-red), var(--band-red-dark));
    color: #fff; font-size: 16px;
  }
  .footer-date { position: absolute; left: 72px; top: 9px; }
  .page-number { position: absolute; right: 72px; top: 9px; }
  .below-footer {
    position: absolute; left: 0; top: 875px; width: 1200px; height: 25px;
    background: var(--below-footer);
  }
</style>
</head>
<body>
  <header class="title-band">
    <h1 class="slide-title">Slide title</h1>
  </header>

  <ul class="body-text">
    <li>Lorem ipsum dolor sit amet, consectetur adipiscing elit.<br>Etiam tempor ornare semper.</li>
    <li>Nunc porta aliquet dolor, et congue sapien ullamcorper porta.</li>
    <li>Donec eleifend nunc a tortor bibendum et iaculis sem scelerisque.
      <ul class="sub-list">
        <li>Nulla et lorem arcu, id lacinia lacus. Proin in lorem urna, interdum volutpat purus. Integer faucibus mauris aliquam felis lacinia in adipiscing nisi dapibus.</li>
        <li>Aenean volutpat massa ac mi accumsan vehicula.</li>
      </ul>
    </li>
    <li>Nullam at elementum elit. Ut pellentesque eros at nisl bibendum sit amet porttitor ante congue.</li>
  </ul>

  <figure class="chart-frame">
    <svg width="466" height="528" viewBox="0 0 466 528" role="img" aria-label="Doughnut chart: 1st Qtr 59%, 2nd Qtr 23%, 3rd Qtr 10%, 4th Qtr 8%">
      <defs>
        <filter id="ring-shadow" x="-20%" y="-20%" width="140%" height="140%">
          <feDropShadow dx="2" dy="3" stdDeviation="3" flood-color="#000" flood-opacity="0.3"/>
        </filter>
      </defs>
      <text x="241" y="47" text-anchor="middle" font-family="Carlito, Calibri, sans-serif" font-size="30" fill="var(--chart-title)">Chart Title</text>
      <g class="donut" filter="url(#ring-shadow)">
        <path fill="var(--q1)" d="M241 108 A184 184 0 1 1 142.4 447.4 L191.7 369.7 A92 92 0 1 0 241 200 Z"/>
        <path fill="var(--q2)" d="M142.4 447.4 A184 184 0 0 1 74.5 213.7 L157.8 252.8 A92 92 0 0 0 191.7 369.7 Z"/>
        <path fill="var(--q3)" d="M74.5 213.7 A184 184 0 0 1 152.3 130.8 L196.7 211.4 A92 92 0 0 0 157.8 252.8 Z"/>
        <path fill="var(--q4)" d="M152.3 130.8 A184 184 0 0 1 241 108 L241 200 A92 92 0 0 0 196.7 211.4 Z"/>
      </g>
      <g class="slice-labels" font-family="Carlito, Calibri, sans-serif" font-size="19" fill="#fff" text-anchor="middle">
        <text x="379" y="322">1st Qtr</text><text x="379" y="351">59%</text>
        <text x="111" y="328">2nd Qtr</text><text x="111" y="357">23%</text>
        <text x="137" y="194">3rd Qtr</text><text x="137" y="222">10%</text>
        <text x="206" y="153">4th Qtr</text><text x="206" y="180">8%</text>
      </g>
    </svg>
  </figure>

  <footer class="footer-band">
    <span class="footer-date">21-11-2011</span>
    <span class="page-number">3</span>
  </footer>
  <div class="below-footer"></div>
</body>
</html>
```